Small 50 Sec Giveaway Video Ad

**image that looks like me**
“Hello this is Doran from Marlowbrook Estate Liquidation & Auction. 2020 has shown us a lot, if 2020 was a kid from school it would be that annoying jerk that waits until your not looking, runs up, and kicks you between the legs and runs away. But the most important thing is that 2020 has led people to lose jobs, homes, and in some cases loved ones. Instead of going along with Govener Pembrack we at Marlowbrook Estate Liquidation & Auction want to help you this Thanksgiving. We want to offer up 10 turkeys and 10 $25 gift cards for raffle! Any one that registers with our online auctions Fridays-Tuesdays every week now through November 24th at https://marlowbrookestate.bidvantor.com/auctions/ will get an entry into the raffle. If you win an item you will get an additional raffle entry! So lets kick your Thanksgiving off with a bang!”
**have the image of me shooting a packaged up grocery store turkey with shotgun**

Industry/Entity Type

Auction

Font styles to use
Serif

Requirements
Must have
• what is within the description
Nice to have
• some highlight of what the giveaway is. maybe a cut to some kind of visual showing 10x an image of a store turkey and 10x a gift card or something

```html
<!DOCTYPE html>
<html lang="en">
<head>
<meta charset="utf-8">
<title>Marlowbrook Estate Liquidation &amp; Auction – Thanksgiving Giveaway</title>
<link rel="stylesheet" href="https://fonts.googleapis.com/css2?family=Cinzel:wght@400&family=Pinyon+Script&family=Montserrat:wght@700&display=swap">
<style>
  :root {
    --bg-chartreuse: #d6d544;
    --shadow-olive: #5f7a1c;
    --ink-navy: #2b5874;
    --teal: #11b6b6;
    --photo-warm: #c9b3a4;
    --photo-plaid: #b94a4a;
    --photo-dark: #2c2a30;
    --photo-grey: #a9adb8;
  }
  * { margin: 0; padding: 0; box-sizing: border-box; }
  html, body {
    width: 1200px;
    height: 675px;
    overflow: hidden;
    background: var(--bg-chartreuse);
  }
  .ad-frame {
    position: relative;
    width: 1200px;
    height: 675px;
    background: var(--bg-chartreuse);
    overflow: hidden;
  }
  .hosts-photo {
    position: absolute;
    left: 0;
    top: 0;
    width: 540px;
    height: 675px;
  }
  .brand-name {
    position: absolute;
    left: 640px;
    top: 246px;
    width: 480px;
    text-align: center;
    font-family: "Cinzel", serif;
    font-weight: 400;
    font-size: 33px;
    line-height: 1.35;
    letter-spacing: 0.02em;
    color: var(--ink-navy);
  }
  .headline-script {
    position: absolute;
    left: 490px;
    top: 370px;
    font-family: "Pinyon Script", cursive;
    font-size: 118px;
    line-height: 1;
    color: var(--ink-navy);
    white-space: nowrap;
  }
  .headline-bold {
    position: absolute;
    left: 514px;
    top: 484px;
    font-family: "Montserrat", sans-serif;
    font-weight: 700;
    font-size: 134px;
    line-height: 1;
    letter-spacing: -0.01em;
    color: var(--teal);
    white-space: nowrap;
  }
</style>
</head>
<body>
  <main class="ad-frame">
    <svg class="hosts-photo" viewBox="0 0 540 675" role="img" aria-label="Photo of the two hosts, a woman in glasses and a grey sweater and a bearded man in a plaid shirt, smiling outdoors">
      <defs>
        <linearGradient id="photoTones" x1="0" y1="0" x2="1" y2="1">
          <stop offset="0" stop-color="var(--photo-warm)"/>
          <stop offset="0.45" stop-color="var(--photo-plaid)"/>
          <stop offset="0.7" stop-color="var(--photo-dark)"/>
          <stop offset="1" stop-color="var(--photo-grey)"/>
        </linearGradient>
      </defs>
      <path class="photo-shadow" fill="var(--shadow-olive)" d="M0 70 L40 55 L120 50 L210 40 L280 0 L480 0 L490 130 L470 190 L515 230 L525 420 L470 470 L420 540 L395 675 L0 675 Z"/>
      <path class="photo-fill" fill="url(#photoTones)" d="M0 60 L35 48 L115 42 L200 34 L268 0 L470 0 L478 125 L458 185 L503 225 L512 412 L460 462 L408 532 L382 675 L0 675 Z"/>
    </svg>

    <p class="brand-name">Marlowbrook Estate<br>Liquidation &amp; Auction</p>

    <h1 class="headline">
      <span class="headline-script">Thanksgiving</span>
      <span class="headline-bold">Giveaway</span>
    </h1>
  </main>
</body>
</html>
```